Brightpath Letterhead

We would like a letterhead for our company. I have uploaded our logo.

Brightpath Ridge Consulting
1450 W Corliss Ave Ste 310
Arlington, TX 76006
833-517-2906

```html
<!DOCTYPE html>
<html lang="en">
<head>
<meta charset="utf-8">
<title>Brightpath Ridge Consulting Letterhead</title>
<link href="https://fonts.googleapis.com/css2?family=Source+Sans+3:wght@400;600;700&family=Arimo:wght@400&display=swap" rel="stylesheet">
<style>
  :root {
    --backdrop: #d8d9db;
    --paper: #fbfbfb;
    --paper-shade: #efefef;
    --teal: #165d6b;
    --ink: #555a5e;
    --ink-soft: #5f6367;
    --on-teal: #ffffff;
  }
  * { margin: 0; padding: 0; box-sizing: border-box; }
  html, body {
    width: 1200px; height: 1141px; overflow: hidden;
    background: var(--backdrop);
  }
  .sheet {
    position: absolute; left: 333px; top: 87px;
    width: 675px; height: 949px;
    background: linear-gradient(160deg, var(--paper) 40%, var(--paper-shade) 100%);
    box-shadow: 0 2px 6px rgba(0,0,0,0.18);
    overflow: hidden;
  }
  .header-wave { position: absolute; left: 0; top: 0; width: 675px; height: 160px; }
  .sender {
    position: absolute; left: 49px; top: 40px;
    font-family: "Source Sans 3", sans-serif; font-style: normal;
    color: var(--on-teal);
    font-size: 12.7px; line-height: 15.7px;
  }
  .sender .phone { margin-top: 6px; font-size: 15px; font-weight: 700; letter-spacing: 0.2px; }
  .brand-name {
    position: absolute; left: 385px; top: 84px;
    font-family: "Source Sans 3", sans-serif; font-weight: 400;
    color: var(--teal); font-size: 17px; line-height: 1;
  }
  .letter {
    position: absolute; left: 50px; top: 306px; width: 575px;
    font-family: "Arimo", sans-serif; color: var(--ink);
  }
  .salutation { font-size: 16px; color: var(--ink-soft); margin-bottom: 27px; }
  .letter p {
    font-size: 9.7px; line-height: 14.5px; text-align: justify;
    margin-bottom: 14px;
  }
  .closing { font-size: 9.7px; margin-top: 22px; }
  .signature {
    margin-top: 12px; width: 72px; height: 24px;
    background: linear-gradient(90deg, rgba(40,44,52,0.18), rgba(40,44,52,0.06));
    border-radius: 3px;
  }
</style>
</head>
<body>
  <main class="sheet">
    <svg class="header-wave" viewBox="0 0 675 160" aria-hidden="true">
      <path fill="var(--teal)" d="M0 0 H675 V20 C620 8 560 5 520 12 C440 25 380 72 320 105 C260 136 210 150 160 150 C100 150 50 142 0 130 Z"/>
    </svg>

    <address class="sender">
      <div class="sender-name">Brightpath Ridge Consulting</div>
      <div class="sender-street">1450 W Corliss Ave Ste 310</div>
      <div class="sender-city">Arlington, TX 76006</div>
      <div class="phone">833-517-2906</div>
    </address>

    <div class="brand-name">Brightpath Ridge Consulting</div>

    <section class="letter">
      <div class="salutation">Dear Mr. Calloway,</div>
      <p>Lorem ipsum dolor sit amet, consectetur adipiscing elit. Donec orci purus, luctus vitae dignissim eu, iaculis sed purus. Vivamus faucibus, ipsum nec aliquet viverra, leo mauris condimentum ligula, sit amet sagittis enim ligula quis arcu. Nam egestas tortor id nisi porttitor mattis. In tortor ante, ultricies in suscipit a, tempus non massa. Vivamus et auctor mi. Fusce vel massa nulla. Phasellus nec eros mauris, et scelerisque orci.</p>
      <p>Donec malesuada orci vitae nulla accumsan porta a id massa. Quisque accumsan iaculis magna sit amet fringilla. Maecenas consequat, magna eget tincidunt semper, odio nibh rutrum mi, id feugiat ante nisi eu risus. Vestibulum nunc orci, rhoncus a placerat in, ultricies in mi. Cras mattis varius eros, vel fringilla nisi suscipit eget. Quisque scelerisque sagittis nulla at porttitor.</p>
      <p>Sed id augue vitae urna euismod commodo aliquet a quam. Pellentesque arcu velit, cursus et malesuada ut, consequat et diam. Nullam erat sem, rhoncus id ullamcorper vitae, rhoncus et arcu. In ultricies ultricies nulla, ut rutrum nisi iaculis at. Donec eu magna a metus ornare faucibus. Fusce aliquet faucibus ultricies. Morbi semper, est id tincidunt gravida, sem arcu adipiscing lacus, ac bibendum nulla leo eu purus. Quisque nec diam sed risus consectetur a ccumsan quis quis nibh. Vestibulum id purus lorem.</p>
      <p>It is a long established fact that a reader will be distracted by the readable content of a page when looking at its layout. The point of using Lorem Ipsum is that it has a more-or-less normal distribution of letters, as opposed to using 'Content here, content here', making it look like readable English. Many desktop publishing packages</p>
      <p>ada ut, consequat et diam. Nullam erat sem, rhoncus id ullamcorper vitae, rhoncus et arcu. In ultricies ultricies nulla, ut rutrum nisi iaculis at. Donec eu magna a metus ornare faucibus. Fusce aliquet faucibus ultricies. Morbi semper,</p>
      <div class="closing">Sincerely,</div>
      <div class="signature" role="img" aria-label="Handwritten signature"></div>
    </section>
  </main>
</body>
</html>
```